We need a fresh, new church business card!!

We need a church business card with basic info to hand out as invites. We are looking for something clean that communicates our basic information clearly.

We are open to square or rectangle card sizes.

General Public

Religious

The attached logo is the only one that I have available. We'd like to see options with with text of the logo lighter and on a dark background as well as options with white/light backgrounds.

Also, we'd like to see option with rounded corners.

• Address - 2718 Maple Row, Rockford, IL 61142
• Website - brookvane.example
• Phone - 815-555-0163
• Service times -
• Sunday - 10am Sunday School
• - 11am Family Worship
• - 6pm Night of Prayer
• Wednesday - 7:30pm Adult Bible Study
• Classes for all ages

```html
<!DOCTYPE html>
<html lang="en">
<head>
<meta charset="utf-8">
<title>Brookvane Pentecostal Church – Business Card</title>
<link rel="stylesheet" href="https://fonts.googleapis.com/css2?family=Open+Sans:ital,wght@0,400;0,700;1,700&family=Roboto+Slab:wght@400;500&display=swap">
<style>
  :root {
    --teal: #5a93a3;
    --teal-dark: #4f8797;
    --paper: #ffffff;
    --ink: #3a3a3a;
    --muted: #6f6f6f;
    --backdrop: #ecebe8;
    --shadow: rgba(0, 0, 0, 0.28);
  }
  * { box-sizing: border-box; margin: 0; padding: 0; }
  html, body { width: 1200px; height: 649px; overflow: hidden; }
  body { background: var(--backdrop); position: relative; }

  .card {
    position: absolute;
    width: 560px;
    height: 320px;
    box-shadow: 0 6px 14px var(--shadow);
  }

  /* Back of card */
  .card-back {
    left: 142px; top: 115px;
    background: var(--teal);
    color: var(--paper);
    font-family: "Open Sans", sans-serif;
    text-align: center;
  }
  .back-brand {
    position: absolute; left: 0; right: 0; top: 82px;
    display: flex; flex-direction: column; align-items: center; gap: 14px;
  }
  .back-brand .dot {
    width: 70px; height: 70px; border-radius: 50%; background: var(--paper);
  }
  .back-brand .name {
    font-family: "Roboto Slab", serif; font-weight: 400;
    font-size: 22px; letter-spacing: 2px; text-transform: uppercase;
  }
  .schedule {
    position: absolute; left: 0; right: 0; top: 238px;
    font-size: 14px; line-height: 21px;
  }
  .schedule strong { font-weight: 700; }
  .back-web {
    position: absolute; left: 58px; right: 58px; top: 282px;
    display: flex; align-items: center; gap: 8px;
    font-weight: 700; font-style: italic; font-size: 14px; letter-spacing: 2px;
  }
  .back-web::before, .back-web::after {
    content: ""; flex: 1; height: 1px; background: var(--paper);
  }

  /* Front of card */
  .card-front {
    left: 557px; top: 235px;
    background: var(--paper);
    font-family: "Roboto Slab", serif;
    color: var(--ink);
  }
  .front-brand {
    position: absolute; right: 24px; top: 28px;
    display: flex; align-items: center; gap: 10px;
  }
  .front-brand .dot {
    width: 44px; height: 44px; border-radius: 50%; background: var(--teal);
  }
  .front-brand .name {
    font-weight: 400; font-size: 17px; line-height: 22px;
    color: var(--teal-dark); letter-spacing: 1px; text-transform: uppercase;
  }
  .person { position: absolute; left: 24px; top: 150px; }
  .person-name {
    font-weight: 400; font-size: 21px; letter-spacing: 1px;
    color: var(--teal); text-transform: uppercase;
  }
  .person-role { font-size: 15px; color: var(--muted); margin-top: 4px; }
  .contact { list-style: none; margin-top: 12px; font-size: 15px; }
  .contact li { display: flex; align-items: center; gap: 8px; height: 23px; }
  .contact svg { width: 13px; height: 13px; fill: var(--teal); flex: none; }
  .address { font-size: 15px; margin-top: 6px; }
</style>
</head>
<body>

<section class="card card-back">
  <div class="back-brand">
    <span class="dot"></span>
    <span class="name">Brookvane</span>
  </div>
  <div class="schedule">
    <p><strong>Sunday:</strong> 10am Sunday School, 11am Family Worship, 6pm Night of Prayer</p>
    <p><strong>Wednesday:</strong> 7:30pm Adult Bible Study, Classes for all ages</p>
  </div>
  <p class="back-web">www.brookvane.example</p>
</section>

<section class="card card-front">
  <div class="front-brand">
    <span class="dot"></span>
    <span class="name">Brookvane<br>Pentecostal Church</span>
  </div>
  <div class="person">
    <h1 class="person-name">Daniel Reyes</h1>
    <p class="person-role">CEO/Founder</p>
    <ul class="contact">
      <li>
        <svg viewBox="0 0 16 16" aria-hidden="true"><path d="M3.6 1.2l2.3 2.6-1.3 2a9 9 0 0 0 5.6 5.6l2-1.3 2.6 2.3-1.5 2.4C7.5 14.6 1.4 8.5 1.2 2.7z"/></svg>
        815-555-0163
      </li>
      <li>
        <svg viewBox="0 0 16 16" aria-hidden="true"><path d="M1 3h14v1.2L8 8.6 1 4.2z"/><path d="M1 5.6l7 4.4 7-4.4V13H1z"/></svg>
        info@brookvane.example
      </li>
      <li>
        <svg viewBox="0 0 16 16" aria-hidden="true"><circle cx="8" cy="8" r="7"/></svg>
        www.brookvane.example
      </li>
    </ul>
    <p class="address">2718 Maple Row, Rockford, IL 61142</p>
  </div>
</section>

</body>
</html>
```